Daddy's Hour Classes for new fathers

I need a flyer for new dads that will appeal to new dads to come to a 2-hr class about fatherhood and child development.

I am a therapist and educator and I run classes for dads.

I will need to over lay some text over the flyer regarding the details of where and when the class is.

In essence the Flyer needs to promote:
"Daddy's Hour" in bold and large lettering
with 'TM" the trademark symbol beside it in small font and up beside "Daddys Hour".

Here is the text required - it's also on a file uploaded!:
Daddy’s Hour TM – getting into fatherhood

New-Father classes for dads and dads-to-be, run by Ned Brannock

What you’ll get from the 2-hour class:
• Baby-basics - a simple way to understand how to know what your baby needs
• Bonding with your baby
• How to nurture your baby’s developing brain during the biggest period of brain-growth.
• How to give your child the twin-benefits of an attachment system.
• How to make the Work-Life-Relationship balance work after a baby!
• Strategies for managing stress.
Plus hearing from other dads.

About the presenter
The daddy’s hour classes are run by Edward Brannock, a fathers-educator who has run classes for dads for more than 10 years. He is a father of two and has consults around fatherhood issues. He has also presented at conferences and trains midwives and maternal child health nurses on father-inclusive practice Ned has also appeared on tv and radio and in print around the topic of fatherhood..
and his work has can be found on: http://growingkidsplace.example.au/pa_notes_expecting/pa_notes_on_expecting.html a & www.papacheckin.example.au/

Feedback from dads:
"Very impressed - exceeded expectations."
"Some things tonight I had never considered. Helping in later child development, looking at things from different angles."
"The discussion on brain development - the way it was explained - it's good, I would recommend it to others."

Enrol now at: www.edwardbrannock.example.au/daddys-hour.html

www.edwardbrannock.example.au/daddys-hour

THANKS FOR YOUR INTEREST - LOOK FORWARD TO SEEING YOUR GREAT WORK!

Target Market(s)

Dads and dads-to-be who want to learn more about fatherhood so that they get off to a great start as a dad.

Industry/Entity Type

Health

Requirements
Nice to have
• If you think it's too text heavy, ditch the text and I can put it on the website.

Go with your creative instinct!

```html
<!DOCTYPE html>
<html lang="en">
<head>
<meta charset="utf-8">
<title>Daddy’s Hour – Getting into Fatherhood</title>
<link rel="stylesheet" href="https://fonts.googleapis.com/css2?family=Oswald:wght@700&family=Roboto+Condensed:wght@700&family=Arimo:ital,wght@0,400;0,700;1,400&display=swap">
<style>
  :root {
    --page: #ffffff;
    --paper: #e5e0cd;
    --rust: #a0540f;
    --ink: #1d1b18;
    --band: #a8936a;
    --rule: #ffffff;
    --photo-sky: #d9e4df;
    --photo-leaf: #6f9257;
    --photo-shirt: #a9c3d6;
  }
  * { margin: 0; padding: 0; box-sizing: border-box; }
  html, body { width: 941px; height: 1200px; overflow: hidden; background: var(--page); }
  .flyer {
    position: absolute; left: 46px; top: 0;
    width: 848px; height: 1200px;
    background: var(--paper);
    font-family: "Arimo", Arial, sans-serif;
    color: var(--ink);
    overflow: hidden;
  }
  .hero-photo {
    position: absolute; left: 505px; top: 0;
    width: 343px; height: 714px;
    border-left: 5px solid var(--rule);
    border-bottom: 5px solid var(--rule);
    border-bottom-left-radius: 24px;
    background:
      radial-gradient(ellipse 70% 45% at 55% 72%, var(--photo-shirt) 0 60%, transparent 62%),
      linear-gradient(180deg, var(--photo-leaf) 0%, var(--photo-sky) 35%, var(--photo-leaf) 70%, #8aa27a 100%);
  }
  .title {
    position: absolute; left: 41px; top: 40px;
    font-family: "Oswald", "Arial Narrow", sans-serif;
    font-weight: 700; font-size: 60px; line-height: 66px;
    color: var(--rust); text-transform: uppercase;
    text-shadow: 1px 2px 3px rgba(0,0,0,0.35);
    letter-spacing: 0.5px;
  }
  .title .tm {
    font-size: 20px; line-height: 1;
    vertical-align: top; position: relative; top: 10px;
    margin-left: 2px;
  }
  .subtitle {
    position: absolute; left: 41px; top: 312px; width: 450px;
    font-weight: 700; font-size: 17px; line-height: 21px;
  }
  .section-heading {
    position: absolute; left: 41px;
    font-family: "Roboto Condensed", "Arial Narrow", sans-serif;
    font-weight: 700; font-size: 32px; line-height: 34px;
    color: var(--rust);
  }
  .heading-benefits { top: 368px; }
  .heading-presenter { top: 702px; }
  .heading-feedback { top: 940px; }
  .benefits {
    position: absolute; left: 41px; top: 448px; width: 450px;
    list-style: none; font-size: 16.5px; line-height: 21px;
  }
  .benefits li { position: relative; padding-left: 18px; }
  .benefits li::before {
    content: ""; position: absolute; left: 0; top: 5px;
    width: 11px; height: 11px; background: var(--rust);
  }
  .benefits .extra { padding-left: 18px; }
  .benefits .extra::before { display: none; }
  .presenter-bio {
    position: absolute; left: 41px; top: 752px; width: 770px;
    font-size: 17px; line-height: 22px;
  }
  .presenter-links {
    position: absolute; left: 41px; top: 866px; width: 780px;
    font-size: 17px; line-height: 22px;
  }
  .feedback {
    position: absolute; left: 41px; top: 1004px; width: 780px;
    display: flex; gap: 0;
    font-style: italic; font-size: 17px; line-height: 22px;
  }
  .feedback blockquote:nth-child(1) { width: 226px; }
  .feedback blockquote:nth-child(2) { width: 302px; }
  .feedback blockquote:nth-child(3) { width: 250px; }
  .enrol-band {
    position: absolute; left: 0; top: 1110px; width: 848px; height: 90px;
    background: var(--band);
    border-top: 4px solid var(--rule);
    padding: 20px 0 0 48px;
    font-weight: 700; font-size: 19px; line-height: 24px;
  }
</style>
</head>
<body>
<main class="flyer">
  <div class="hero-photo" role="img" aria-label="Photo of a smiling young father carrying his toddler son on his shoulders outdoors"></div>

  <h1 class="title">Daddy’s<br>Hour<sup class="tm">TM</sup> –<br>Getting into<br>Fatherhood</h1>

  <p class="subtitle">New-Father classes for dads and dads-to-be, run by Ned Brannock</p>

  <h2 class="section-heading heading-benefits">What you’ll get<br>from the 2-hour class:</h2>
  <ul class="benefits">
    <li>Baby-basics - a simple way to understand how to know what your baby needs</li>
    <li>Bonding with your baby</li>
    <li>How to nurture your baby’s developing brain during the biggest period of brain-growth.</li>
    <li>How to give your child the twin-benefits of an attachment system.</li>
    <li>How to make the Work-Life-Relationship balance work after a baby!</li>
    <li>Strategies for managing stress.</li>
    <li class="extra">Plus hearing from other dads.</li>
  </ul>

  <h2 class="section-heading heading-presenter">About the presenter</h2>
  <p class="presenter-bio">The daddy’s hour classes are run by Edward Brannock, a fathers-educator who has run classes for dads for more than 10 years. He is a father of two and has consults around fatherhood issues. He has also presented at conferences and trains midwives and maternal child health nurses on father-inclusive practice Ned has also appeared on tv and radio and in print around the topic of fatherhood..</p>
  <p class="presenter-links">And his work has can be found on:<br>http://growingkidsplace.example.au/pa_notes_expecting/pa_notes_on_expecting.html<br>http://www.papacheckin.example.au/</p>

  <h2 class="section-heading heading-feedback">Feedback from dads:</h2>
  <div class="feedback">
    <blockquote>“Very impressed - exceeded expectations.”</blockquote>
    <blockquote>“Some things tonight I had never considered. Helping in later child development, looking at things from different angles.”</blockquote>
    <blockquote>“The discussion on brain development - the way it was explained - it’s good, I would recommend it to others.”</blockquote>
  </div>

  <footer class="enrol-band">Enrol now at:<br>www.edwardbrannock.example.au/daddys-hour.html</footer>
</main>
</body>
</html>
```